Law Firm Website

We are looking to update our old, tired and very flat website. We have someone who will code and host the site but we need some design inspiration. The website will consist of no more than 2/3 pages, possibly with pop-ups for information. We already have all the blurb. We would like something distinctive, clean and eye-catching, using the purple and white theme that we already use on our firm stationery. Examples uploaded. Current website URL is www.dunmorewillett.example.

Industry/Entity Type

Law Firm

```html
<!DOCTYPE html>
<html lang="en">
<head>
<meta charset="utf-8">
<title>Dunmore + Willett Solicitors</title>
<link href="https://fonts.googleapis.com/css2?family=Ubuntu:wght@300;400;500;700&display=swap" rel="stylesheet">
<style>
:root{
  --purple:#5a3f8f;
  --purple-dark:#4a3478;
  --purple-nav:#7a64ab;
  --ink:#1f2b2a;
  --text:#555;
  --muted:#7a6f93;
  --light:#f8fafa;
  --band:#ececec;
  --line:#dcdcdc;
}
*{margin:0;padding:0;box-sizing:border-box}
html,body{width:1024px;height:1200px;overflow:hidden}
body{font-family:'Ubuntu',sans-serif;background:var(--light);color:var(--text);position:relative}
.top-rule{height:4px;background:var(--purple)}
.header{height:101px;background:#fff;position:relative}
.logo{position:absolute;left:134px;top:22px;color:var(--ink);font-weight:700;line-height:1}
.logo .name{font-size:31px;letter-spacing:.5px}
.logo .sub{font-size:19px;margin:8px 0 0 64px}
.reg{position:absolute;top:44px;padding-left:18px;border-left:1px solid #e3e3e3;height:40px;font-size:11px;color:#8c8c98;line-height:16px}
.reg b{display:block;font-weight:400;color:var(--purple)}
.reg.a{left:584px}.reg.b{left:759px}.reg.b b{font-size:12px}
.nav{height:41px;background:linear-gradient(#8b77b9,#6d569f);border-top:1px solid #9b8cc0;border-bottom:1px solid #5a4388;position:relative}
.nav a{position:absolute;top:0;height:40px;line-height:40px;color:#fff;font-size:13px;text-decoration:none;text-align:center}
.nav a.active{background:rgba(255,255,255,.16);width:114px;left:135px}
.hero{position:absolute;top:146px;left:0;width:1024px;height:432px;background:linear-gradient(100deg,#6f5a9c 0%,#a592d4 35%,#8a6cd1 60%,#6b4fb0 100%)}
.hero h1{position:absolute;left:554px;top:162px;font-weight:300;font-size:29px;line-height:35px;color:#fff}
.card{position:absolute;top:514px;height:183px;background:#fff;border:1px solid #ddd}
.card .photo{position:absolute;left:0;top:0;width:157px;height:182px}
.card .body{position:absolute;left:176px;top:22px;right:12px}
.card h2{font-weight:300;font-size:20px;color:var(--purple);margin-bottom:12px}
.card p{font-size:11.5px;line-height:16px;color:#555}
.btn{display:inline-block;margin-top:14px;margin-left:-2px;padding:0 11px;height:26px;line-height:24px;border:1px solid #d6d6d6;border-radius:13px;background:linear-gradient(#fff,#ececec);font-size:9px;color:#777}
.expertise{position:absolute;top:722px;left:0;width:1024px;text-align:center}
.expertise h2{font-weight:300;font-size:21px;color:#333}
.expertise .lead{width:500px;margin:14px auto 0;font-size:9px;line-height:13px;color:var(--muted)}
.area{position:absolute;width:200px}
.area .icon{position:absolute;left:0;top:0;width:45px;height:45px;background:linear-gradient(#8a73bb,var(--purple-dark))}
.area h3{position:absolute;left:55px;top:4px;font-weight:400;font-size:13px;color:#333;white-space:nowrap}
.area span{position:absolute;left:55px;top:26px;font-size:9px;color:var(--muted);white-space:nowrap}
.quote{position:absolute;top:1006px;left:0;width:1024px;height:87px;background:var(--band);border-top:1px solid var(--line);border-bottom:1px solid var(--line);text-align:center;padding-top:24px;font-style:italic;font-weight:300;font-size:13px;line-height:19px;color:#6b7a86}
.quote b{font-style:normal;font-weight:500;color:#5b6a76}
.footer{position:absolute;top:1093px;left:0;width:1024px;height:80px;background:#fff}
.footer .logo{left:137px;top:18px}
.footer .logo .name{font-size:27px}
.footer .logo .sub{font-size:15px;margin:6px 0 0 54px}
.finfo{position:absolute;font-size:9px;line-height:17.6px;color:#7a6f93}
.finfo svg{position:absolute;left:-19px}
.follow{position:absolute;left:776px;top:15px;font-size:9px;color:#666}
.social{position:absolute;top:36px;width:26px;height:26px}
.bar{position:absolute;top:1173px;left:0;width:1024px;height:27px;background:var(--purple);color:#fff;font-size:9px;line-height:27px}
.bar .copy{position:absolute;left:137px}
.bar a{position:absolute;color:#fff;text-decoration:none}
</style>
</head>
<body>
<div class="top-rule"></div>
<header class="header">
  <div class="logo"><div class="name">Dunmore + Willett</div><div class="sub">Solicitors</div></div>
  <div class="reg a">Regulation Authority<b>NO.730158</b></div>
  <div class="reg b">VAT registered number:<b>418 2907 56</b></div>
</header>
<nav class="nav">
  <a class="active" href="#">Home</a>
  <a href="#" style="left:288px;width:124px">Areas of Expertise</a>
  <a href="#" style="left:430px;width:90px">Daniel Dunmore</a>
  <a href="#" style="left:552px;width:90px">Peter Willett</a>
  <a href="#" style="left:677px;width:90px">Contact Us</a>
</nav>
<section class="hero" role="img" aria-label="Photograph of brass scales of justice in a purple-toned courtroom">
  <h1>Dunmore and Willett Solicitors,<br>for the service you deserve.</h1>
</section>

<article class="card" style="left:136px;width:368px">
  <div class="photo" role="img" aria-label="Portrait photograph of Daniel Dunmore" style="background:linear-gradient(#a9aeb4,#4d5a6c)"></div>
  <div class="body"><h2>Daniel Dunmore</h2>
  <p>Daniel Dunmore qualified as a solicitor in 1987 and spent many years working with a busy commercial practice in North London.</p>
  <span class="btn">Read More</span></div>
</article>
<article class="card" style="left:519px;width:370px">
  <div class="photo" role="img" aria-label="Black and white portrait photograph of Peter Willett" style="background:linear-gradient(#3a3a3a,#9a9a9a)"></div>
  <div class="body" style="left:172px"><h2>Peter Willett</h2>
  <p>Willett has 40 years experience in the law. He has a wide range of exper-tise in commercial and private client matters</p>
  <span class="btn">Read More</span></div>
</article>

<section class="expertise">
  <h2>Our Areas of Expertise</h2>
  <p class="lead">The point of using Lorem Ipsum is that it has a more-or-less normal distribution of letters, as opposed to using 'Con-tent here, content here', making it look like readable English.</p>
</section>

<svg width="0" height="0" style="position:absolute"><defs><symbol id="case" viewBox="0 0 45 45"><rect x="14" y="17" width="17" height="12" rx="1.5" fill="#fff"/><path d="M19 17v-2.5h7V17" fill="none" stroke="#fff" stroke-width="1.6"/><rect x="14" y="22" width="17" height="1.2" fill="#6a52a0"/><rect x="21" y="21" width="3" height="3" fill="#6a52a0"/></symbol></defs></svg>

<div class="area" style="left:136px;top:808px"><div class="icon"><svg width="45" height="45"><use href="#case"/></svg></div><h3>Litigation</h3><span>Private and commercial</span></div>
<div class="area" style="left:329px;top:808px"><div class="icon"><svg width="45" height="45"><use href="#case"/></svg></div><h3>Company Matters</h3><span>Acquisitions &amp; mergers</span></div>
<div class="area" style="left:519px;top:808px"><div class="icon"><svg width="45" height="45"><use href="#case"/></svg></div><h3>Insolvency</h3><span>Private and commercial</span></div>
<div class="area" style="left:712px;top:808px"><div class="icon"><svg width="45" height="45"><use href="#case"/></svg></div><h3>Conveyancing</h3><span>Commercial and Residential</span></div>
<div class="area" style="left:136px;top:866px"><div class="icon"><svg width="45" height="45"><use href="#case"/></svg></div><h3>Wills &amp; Probate</h3><span>Estate planning, disputes</span></div>
<div class="area" style="left:329px;top:866px"><div class="icon"><svg width="45" height="45"><use href="#case"/></svg></div><h3>Landlord &amp; Tenant</h3><span>Agreements and disputes</span></div>
<div class="area" style="left:519px;top:866px"><div class="icon"><svg width="45" height="45"><use href="#case"/></svg></div><h3>Divorce</h3><span>Ancillary relief, children</span></div>
<div class="area" style="left:712px;top:866px"><div class="icon"><svg width="45" height="45"><use href="#case"/></svg></div><h3>Care of the Elderly</h3><span>Powers of Attorney</span></div>
<div class="area" style="left:136px;top:924px"><div class="icon"><svg width="45" height="45"><use href="#case"/></svg></div><h3>Intellectual Property</h3><span>Copyright, patents</span></div>
<div class="area" style="left:329px;top:924px"><div class="icon"><svg width="45" height="45"><use href="#case"/></svg></div><h3>Commercial Crime</h3><span>'White Collar' crime</span></div>
<div class="area" style="left:519px;top:924px"><div class="icon"><svg width="45" height="45"><use href="#case"/></svg></div><h3>Media Law</h3><span>Film, TV, Theatre, Radio</span></div>
<div class="area" style="left:712px;top:924px"><div class="icon"><svg width="45" height="45"><use href="#case"/></svg></div><h3>Commercial / Business</h3><span>Structures, agreements</span></div>

<blockquote class="quote">“The point of using Lorem Ipsum is that it has a more-or-less normal distribution of letters, as opposed to using 'Content here, content here',<br>making it look like readable English.” -<b>John Doe, Company XYZ</b></blockquote>

<footer class="footer">
  <div class="logo"><div class="name">Dunmore + Willett</div><div class="sub">Solicitors</div></div>
  <div class="finfo" style="left:474px;top:8px">
    <svg width="10" height="13" viewBox="0 0 10 13" style="top:3px;left:-18px"><path d="M5 0a4.5 4.5 0 0 0-4.5 4.5C.5 8 5 13 5 13s4.5-5 4.5-8.5A4.5 4.5 0 0 0 5 0zm0 6.3a1.8 1.8 0 1 1 0-3.6 1.8 1.8 0 0 1 0 3.6z" fill="var(--purple)"/></svg>
    Company Name<br>48 Harrow Lane<br>Brookfield, BK 20417</div>
  <div class="finfo" style="left:604px;top:8px">
    <svg width="11" height="11" viewBox="0 0 11 11" style="top:3px"><path d="M2.3 0l1.8 2.6-1 1.3c.7 1.6 2 2.9 3.7 3.7l1.3-1L11 8.7 9.6 11C4.3 10.7.3 6.7 0 1.4z" fill="var(--purple)"/></svg>
    <svg width="12" height="9" viewBox="0 0 12 9" style="top:22px"><rect width="12" height="9" fill="var(--purple)"/><path d="M0 0l6 5 6-5" fill="none" stroke="#fff" stroke-width="1"/></svg>
    Phone: +000 318 642<br>contact@dunmorewillett.example</div>
  <div class="follow">Follow Us</div>
  <div class="social" style="left:778px;background:#3b5a9a" role="img" aria-label="Social profile link"></div>
  <div class="social" style="left:816px;background:#2fa3dc" role="img" aria-label="Social profile link"></div>
  <div class="social" style="left:854px;background:#1a70a8" role="img" aria-label="Social profile link"></div>
</footer>
<div class="bar">
  <span class="copy">Copyright 2014 Dunmore + Willett | All Rights Reserved</span>
  <a href="#" style="left:604px">Home</a>
  <a href="#" style="left:651px">Services</a>
  <a href="#" style="left:704px">Locations</a>
  <a href="#" style="left:765px">Partners</a>
  <a href="#" style="left:820px">FAQ</a>
  <a href="#" style="left:856px">Contact</a>
</div>
</body>
</html>
```